Large multi-office optometry business opening a Dry Eye Spa and needs sign.

Business name/sign info: Brenwick Dry Eye Institute, (555) 362-4817
Backlit pole sign at office entrance on a very busy street
Sign dimensions: 53" tall x 136.5" wide
State of the art Dry Eye Spa for treatment of all forms of dry eye and ocular surface disease. Also, have aesthetics treatments (IPL, Low Level Light Treatment, etc.)

Target Market(s)

People who are suffering from: dryness, burning, foreign body sensation, itching, fluctuating vision, tired eyes, etc.

Industry/Entity Type

Optometry and aesthetics

Colors
0054AA
0677BA
7BADD7
CADEEF
E8F1F8

Requirements
Must have
• Business name, phone number, subliminal message of relief in a glance or short look.
Nice to have
• Cool, relief, soothing sense.
Should not have
• Too much information or too busy.

```html
<!DOCTYPE html>
<html lang="en">
<head>
<meta charset="utf-8">
<title>Brenwick Dry Eye Institute – Pole Sign</title>
<link rel="stylesheet" href="https://fonts.googleapis.com/css2?family=Bebas+Neue&display=swap">
<style>
  :root {
    --backdrop: #8a8a8a;
    --sign-bg: #f6f8fa;
    --brand-deep: #1a4fa0;
    --brand-mid: #3090cf;
    --brand-light: #9ccbe6;
    --brand-navy: #242a68;
    --brand-blue: #1d4a9a;
    --phone-ink: #223a80;
    --rule: #b9b9bd;
  }
  * { margin: 0; padding: 0; box-sizing: border-box; }
  html, body {
    width: 1200px; height: 2583px; overflow: hidden;
    background: var(--backdrop);
  }
  /* 136.5 x 53 in landscape ratio */
  .sign {
    position: absolute; left: 20px; top: 1066px;
    width: 1160px; height: 450px;
    background: var(--sign-bg);
    overflow: hidden;
    font-family: "Bebas Neue", "Oswald", sans-serif;
  }
  .sign__art { position: absolute; inset: 0; width: 100%; height: 100%; }
  .sign__copy {
    position: absolute; left: 430px; top: 0; width: 700px;
    text-align: center;
  }
  .sign__text { position: absolute; left: 0; width: 100%; line-height: 1; white-space: nowrap; }
  .eyebrow {
    top: 30px; font-size: 56px; color: var(--brand-deep);
    display: flex; justify-content: center; align-items: center; gap: 18px;
  }
  .eyebrow::before, .eyebrow::after {
    content: ""; width: 44px; height: 3px; background: var(--rule); margin-top: -6px;
  }
  .title { top: 92px; font-size: 100px; color: var(--brand-mid); font-weight: 400; }
  .divider {
    position: absolute; top: 204px; left: 40px; width: 620px; height: 3px;
    background: linear-gradient(90deg, transparent, #a9a7ad 50%, transparent);
  }
  .phone { top: 224px; font-size: 80px; color: var(--phone-ink); }
</style>
</head>
<body>
  <main class="sign">
    <svg class="sign__art" viewBox="0 0 1160 450" aria-hidden="true">
      <defs>
        <radialGradient id="mark-fill" cx="50%" cy="55%" r="60%">
          <stop offset="0" stop-color="#3d5aa8"/>
          <stop offset="0.55" stop-color="#3090cf"/>
          <stop offset="1" stop-color="#7bb6df"/>
        </radialGradient>
      </defs>
      <path class="wave wave--light" fill="var(--brand-light)"
        d="M0 330 C120 300 260 300 420 330 C700 360 980 300 1160 250 V450 H0Z"/>
      <path class="wave wave--mid" fill="var(--brand-mid)"
        d="M0 360 C140 380 300 350 460 355 C720 362 960 350 1160 330 V450 H0Z"/>
      <path class="wave wave--deep" fill="var(--brand-blue)"
        d="M0 392 L420 380 C700 372 960 385 1160 368 V450 H0Z"/>
      <path class="wave wave--navy" fill="var(--brand-navy)"
        d="M0 405 C300 396 700 392 1160 400 V450 H0Z"/>
      <g role="img" aria-label="Emblem area: blue water droplet containing a stylised eye">
        <circle cx="220" cy="225" r="186" fill="var(--sign-bg)"/>
        <circle cx="220" cy="225" r="166" fill="url(#mark-fill)"/>
      </g>
    </svg>

    <div class="sign__copy">
      <p class="sign__text eyebrow">Brenwick</p>
      <h1 class="sign__text title">Dry Eye Institute</h1>
      <div class="divider"></div>
      <p class="sign__text phone">(555) 362-4817</p>
    </div>
  </main>
</body>
</html>
```